Engineering group involved with fire safety needs a business card

We need a business card design for a company based in Greece called "Varotis Group". We are engineers and specialized technicians, operating the following : a) Fire fighting equipment trade b) Installation , Inspection & Maintenance of fire extinguishers and fire protection systems c) Occupational Health & Safety (Risk assessment & management/ Staff training). We need a clear and simple card design. I uploaded a draft I made, in order to give you an idea of the company and how I currently imagine the design of the card. I also uploaded the logo in .png file format. We are always open to different, new suggestions and ideas you may want to submit.
Target Market(s)
industries, companies, managers, retail clients
Industry/Entity Type
Fire Safety
Contact Information for Business Card
Addresses & phone numbers (headquarters + branch), logo, name (you can find all the details on the uploaded files!)
Colors
Designer to choose colors to be used in the design.
Look and feel
Each slider illustrates characteristics of the customer's brand and the style your logo design should communicate.

```html
<!DOCTYPE html>
<html lang="en">
<head>
<meta charset="utf-8">
<title>Varotis Group – Business Card</title>
<link rel="stylesheet" href="https://fonts.googleapis.com/css2?family=Open+Sans:wght@400;700&display=swap">
<style>
  :root{
    --backdrop:#6fb0a6;
    --card-white:#ffffff;
    --card-black:#0b0b0b;
    --brand-red:#b11f26;
    --brand-grey:#5d6063;
    --text-dark:#3a3a3a;
  }
  html,body{margin:0;padding:0;overflow:hidden;}
  body{
    width:1200px;height:856px;
    background:var(--backdrop);
    font-family:"Open Sans",Arial,sans-serif;
    display:flex;align-items:center;justify-content:center;gap:60px;
  }
  .card{
    position:relative;width:500px;height:286px;border-radius:26px;overflow:hidden;
    box-shadow:0 10px 28px rgba(0,0,0,.22);
  }
  /* Front */
  .card--front{background:var(--card-white);}
  .front__band{position:absolute;left:0;bottom:0;width:500px;height:286px;}
  .brand{position:absolute;left:48px;top:38px;display:flex;align-items:center;gap:10px;}
  .brand__mark{width:18px;height:18px;background:var(--brand-red);}
  .brand__name{font-weight:700;font-size:22px;color:var(--brand-red);letter-spacing:.5px;}
  .contacts{position:absolute;left:52px;top:92px;list-style:none;margin:0;padding:0;}
  .contacts__item{display:flex;align-items:center;gap:10px;font-size:14px;color:var(--text-dark);height:26px;}
  .contacts__icon{width:16px;height:16px;flex:none;}
  .person{position:absolute;right:40px;top:100px;text-align:right;}
  .person__name{font-weight:700;font-size:21px;color:var(--brand-red);margin:0;line-height:1.1;}
  .person__role{font-size:20px;color:var(--brand-grey);margin:0;line-height:1.1;}
  /* Back */
  .card--back{background:var(--card-black);display:flex;align-items:center;justify-content:center;gap:14px;}
  .back__mark{width:26px;height:26px;background:var(--card-white);}
  .back__name{font-weight:700;font-size:40px;color:var(--card-white);letter-spacing:1px;}
</style>
</head>
<body>
  <section class="card card--front" aria-label="Business card front">
    <svg class="front__band" viewBox="0 0 500 286" aria-hidden="true">
      <path d="M0 262 L250 222 Q262 200 282 196 L500 196 L500 286 L0 286 Z" fill="var(--brand-red)"/>
      <path d="M0 266 L252 230 Q266 210 284 206 L500 206 L500 210 L286 210 Q270 214 258 234 L0 272 Z" fill="var(--card-white)"/>
      <path d="M0 272 L258 236 Q262 232 264 230 L0 268 Z" fill="var(--card-white)"/>
      <path d="M0 256 L246 220 L250 222 L0 262 Z" fill="var(--brand-grey)"/>
    </svg>
    <div class="brand">
      <span class="brand__mark"></span>
      <span class="brand__name">VAROTIS GROUP</span>
    </div>
    <ul class="contacts">
      <li class="contacts__item">
        <svg class="contacts__icon" viewBox="0 0 16 16"><rect x=".75" y=".75" width="14.5" height="14.5" fill="none" stroke="var(--brand-red)" stroke-width="1.5"/><path d="M5 4l2 2-1 1.2q1 2 2.8 2.8L10 9l2 2-1.2 1.2Q7 12 4 6.2Z" fill="var(--brand-red)"/></svg>
        +302101234567
      </li>
      <li class="contacts__item">
        <svg class="contacts__icon" viewBox="0 0 16 16"><rect x=".75" y=".75" width="14.5" height="14.5" fill="none" stroke="var(--brand-red)" stroke-width="1.5"/><rect x="3.5" y="5" width="9" height="6" fill="none" stroke="var(--brand-red)" stroke-width="1.2"/><path d="M3.5 5l4.5 3.5L12.5 5" fill="none" stroke="var(--brand-red)" stroke-width="1.2"/></svg>
        info@varotisgroup.gr
      </li>
      <li class="contacts__item">
        <svg class="contacts__icon" viewBox="0 0 16 16"><rect x=".75" y=".75" width="14.5" height="14.5" fill="none" stroke="var(--brand-red)" stroke-width="1.5"/><circle cx="8" cy="8" r="4.5" fill="var(--brand-red)"/><path d="M3.5 8h9M8 3.5v9" stroke="var(--card-white)" stroke-width=".8"/></svg>
        www.varotisgroup.gr
      </li>
      <li class="contacts__item">
        <svg class="contacts__icon" viewBox="0 0 16 16"><rect x=".75" y=".75" width="14.5" height="14.5" fill="none" stroke="var(--brand-red)" stroke-width="1.5"/><path d="M3 8.5L8 4l5 4.5h-1.5V12h-2V9.5h-3V12h-2V8.5Z" fill="var(--brand-red)"/></svg>
        12 Lemonia Street
      </li>
    </ul>
    <div class="person">
      <p class="person__name">Stelios Andrikos</p>
      <p class="person__role">Director</p>
    </div>
  </section>

  <section class="card card--back" aria-label="Business card back">
    <span class="back__mark"></span>
    <span class="back__name">VAROTIS GROUP</span>
  </section>
</body>
</html>
```